Business Card Colourful and fun Design Project

I need a business card design for my Ecommerce website which am launching soon. we are based in the United Arab Emirates and our customers are based in Dubai and other cities in UAE, In addition to our neighbour countries in the GCC. We sell Gadgets, fashion and other trendy stuff that are hard to find in our market. The company name is "ZIPKOALA" logo consists of a panda wearing traditional local Arab thobe. would like to see a clean, colourful fun design to represent us.
Updates
please read the discussion board. thanks
Industry/Entity Type
Fashion
Look and feel
Each slider illustrates characteristics of the customer's brand and the style your logo design should communicate.

```html
<!DOCTYPE html>
<html lang="en">
<head>
<meta charset="utf-8">
<title>ZIPKOALA Business Card</title>
<link rel="stylesheet" href="https://fonts.googleapis.com/css2?family=Open+Sans:wght@400;600&display=swap">
<style>
  :root {
    --stage-bg: #ececec;
    --card-red-light: #b8262a;
    --card-red: #9c1c20;
    --card-red-dark: #6e1114;
    --text-white: #ffffff;
    --rule-white: rgba(255, 255, 255, 0.85);
    --mascot-light: #f4f4f4;
    --mascot-mid: #c9c9c9;
  }
  html, body {
    margin: 0;
    padding: 0;
    width: 1200px;
    height: 1000px;
    overflow: hidden;
    background: var(--stage-bg);
  }
  .canvas {
    position: relative;
    width: 1200px;
    height: 1000px;
  }
  .business-card {
    position: absolute;
    left: 100px;
    top: 215px;
    width: 1000px;
    height: 570px;
    background: radial-gradient(ellipse at 50% 45%, var(--card-red-light) 0%, var(--card-red) 55%, var(--card-red-dark) 100%);
    font-family: "Open Sans", Arial, sans-serif;
    color: var(--text-white);
    overflow: hidden;
  }
  .mascot {
    position: absolute;
    left: 175px;
    top: 85px;
    width: 150px;
    height: 195px;
    border-radius: 12px;
    background: linear-gradient(180deg, var(--mascot-light) 0%, var(--mascot-mid) 100%);
  }
  .brand-name {
    position: absolute;
    left: 360px;
    top: 140px;
    width: 480px;
    margin: 0;
    text-align: center;
    font-size: 66px;
    font-weight: 600;
    letter-spacing: 4px;
    line-height: 1;
    color: var(--text-white);
  }
  .divider {
    position: absolute;
    left: 100px;
    top: 308px;
    width: 800px;
    height: 1px;
    background: var(--rule-white);
  }
  .tagline {
    position: absolute;
    left: 0;
    top: 330px;
    width: 1000px;
    margin: 0;
    text-align: center;
    font-size: 35px;
    font-weight: 400;
    letter-spacing: 1px;
    color: var(--text-white);
  }
</style>
</head>
<body>
  <main class="canvas">
    <section class="business-card">
      <div class="mascot" role="img" aria-label="Mascot illustration: a panda wearing a white traditional thobe and red-patterned headscarf"></div>
      <h1 class="brand-name">ZIPKOALA</h1>
      <div class="divider"></div>
      <p class="tagline">WE SELL STUFF THAT ARE HARD TO FIND</p>
    </section>
  </main>
</body>
</html>
```